A online shop for solid wood need a Stationary design

A new online shop (in Austria and Germany) for solid wood and steel furniture (feldberg-formwerk) needs a Stationay design (letterhead, business card, envelope etc...). Dining tables, coffee tables, TV furniture and similar furniture will be sold. Everything will be custom made.

```html
<!DOCTYPE html>
<html lang="en">
<head>
<meta charset="utf-8">
<title>Feldberg Formwerk – Letterhead</title>
<link href="https://fonts.googleapis.com/css2?family=Lato:wght@400;700;900&family=Great+Vibes&display=swap" rel="stylesheet">
<style>
  :root {
    --brand-red: #e00d17;
    --ink: #2c2c2c;
    --ink-soft: #4a4a4a;
    --paper: #ffffff;
    --backdrop: #e6e6e8;
    --rule-black: #111111;
  }
  * { box-sizing: border-box; margin: 0; padding: 0; }
  html, body { width: 1200px; height: 960px; overflow: hidden; }
  body {
    background: var(--backdrop);
    font-family: "Lato", Arial, sans-serif;
    color: var(--ink);
    position: relative;
  }
  .letterhead {
    position: absolute;
    left: 275px; top: 20px;
    width: 650px; height: 920px;
    background: var(--paper);
    box-shadow: 0 6px 24px rgba(0,0,0,.12);
    overflow: hidden;
  }
  .brand {
    position: absolute; left: 52px; top: 54px;
    font-weight: 900; color: var(--brand-red);
    font-size: 30px; line-height: 1; letter-spacing: 1px;
    text-transform: uppercase;
  }
  .brand-line { display: block; }
  .contact {
    position: absolute; right: 48px; top: 56px;
    border-left: 1.5px solid var(--brand-red);
    padding-left: 12px;
    font-style: normal;
    font-size: 10.5px; line-height: 1.55; color: var(--ink-soft);
  }
  .contact-row { display: flex; align-items: center; gap: 6px; }
  .contact-row svg { width: 9px; height: 9px; fill: var(--brand-red); flex: none; }
  .letter-body {
    position: absolute; left: 70px; top: 200px; width: 520px;
    font-size: 12.5px; line-height: 1.45; color: var(--ink-soft);
  }
  .letter-date { margin-bottom: 18px; font-size: 13.5px; }
  .recipient { margin-bottom: 18px; font-size: 13.5px; }
  .salutation { font-weight: 700; font-size: 16px; color: var(--ink); margin-bottom: 16px; }
  .letter-body p.paragraph { margin-bottom: 18px; }
  .closing { margin-top: 32px; font-size: 13px; }
  .signature {
    font-family: "Great Vibes", cursive;
    font-size: 44px; color: var(--ink); margin-top: 8px; margin-left: 20px;
  }
  .footer-rule {
    position: absolute; left: 0; right: 0; bottom: 40px;
    height: 3px; background: var(--rule-black);
  }
  .footer-band {
    position: absolute; left: 0; right: 0; bottom: 0;
    height: 34px; background: var(--brand-red);
  }
</style>
</head>
<body>
  <main class="letterhead">
    <div class="brand">
      <span class="brand-line">Feldberg</span>
      <span class="brand-line">Formwerk</span>
    </div>

    <address class="contact">
      <div>Postfach 4120</div>
      <div>8010 Graz, Austria</div>
      <div class="contact-row"><svg viewBox="0 0 10 10"><path d="M2 1l2 0 1 2-1.2 1a5 5 0 0 0 2.2 2.2L7 5l2 1v2a1 1 0 0 1-1 1A8 8 0 0 1 1 2a1 1 0 0 1 1-1z"/></svg>0316 482 7719</div>
      <div class="contact-row"><svg viewBox="0 0 10 10"><path d="M0 2h10v6H0z M0 2l5 3.5L10 2" /></svg>info@feldbergformwerk.com</div>
      <div class="contact-row"><svg viewBox="0 0 10 10"><circle cx="5" cy="5" r="5"/></svg>www.feldbergformwerk.com</div>
    </address>

    <section class="letter-body">
      <p class="letter-date">Feb-03-2022</p>
      <p class="recipient">Mr. Jonas Weber<br>President</p>
      <p class="recipient">Arbor Linie GmbH<br>123 Street Name, Suite# 10<br>City, State, 120023</p>
      <p class="salutation">Dear Mr, Jonas</p>
      <p class="paragraph">Lorem ipsum dolor sit amet, consectetur adipisicing elit, sed do eiusmod tempor incididunt ut labore et dolore magna aliqua. Ut enim ad minim veniam, quis nostrud exercitation ullamco laboris nisi ut aliquip ex ea commodo consequat. Duis aute irure dolor in reprehenderit in voluptate velit esse cillum dolore eu fugiat nulla pariatur.</p>
      <p class="paragraph">Lorem ipsum dolor sit amet, consectetur adipisicing elit, sed do eiusmod tempor incididunt ut labore et dolore magna aliqua. Ut enim ad minim veniam, quis nostrud exercitation ullamco laboris nisi ut aliquip ex ea commodo consequat. Duis aute irure dolor in reprehenderit in voluptate velit esse cillum dolore eu fugiat nulla pariatur.</p>
      <p class="paragraph">Lorem ipsum dolor sit amet, consectetur adipisicing elit, sed do eiusmod tempor incididunt ut labore et dolore magna aliqua. Ut enim ad minim veniam, quis nostrud exercitation ullamco laboris nisi ut aliquip ex ea commodo consequat.</p>
      <p class="paragraph">Excepteur sint occaecat cupidatat non proident, sunt in culpa qui officia deserunt mollit anim id est laborum. re et dolore magnam aliquam quaerat voluptatem.</p>
      <p class="closing">Regards</p>
      <p class="signature">Lukas Brenner</p>
    </section>

    <div class="footer-rule" aria-hidden="true"></div>
    <div class="footer-band" aria-hidden="true"></div>
  </main>
</body>
</html>
```